Vero M.Q. - Diagnostic Ultrasound Flyer

About US
Vero M.Q. is a concierge ultrasound company that provides onsite or offsite diagnostic ultrasounds. We have over 14 years experience in sonography, business management, and customer service. We offer both the physician and patient flexibility, convenience, and access to timely services.

We provide ultrasounds for the following specialties:
Obstetrics/Gynecology
Abdominal
Small Parts
Vascular

Company Features:
1. Onsite or Offsite Scans
2. Images Available Immediately for Referring Physician and Patient
3. Flexible Options for Ultrasound Interpretation/Billing
4. Access to Interpreting Radiologist
5. Final Report Process - 1-2 Business Days/ 1 hour for STAT.
6. PACS Storage with Secure Access.

We need a place to add in our contact information (address, email, website, phone)

We already have a logo and would like to use it ( they are attached). We would the colors to match the logo colors....maybe lighter version of yellow and blue.

```html
<!DOCTYPE html>
<html lang="en">
<head>
<meta charset="utf-8">
<title>Vero M.Q. – Diagnostic Ultrasound Flyer</title>
<link rel="stylesheet" href="https://fonts.googleapis.com/css2?family=Montserrat:ital,wght@0,300;0,400;0,500;0,700;0,800;1,700;1,800&display=swap">
<style>
  :root {
    --brand-blue: #1410a8;
    --brand-yellow: #fdbd2c;
    --paper: #ffffff;
    --ink: #1a1a1a;
    --ink-soft: #555a60;
    --backdrop: #7b7b7b;
    --photo-light: #dfe7f2;
    --photo-mid: #b9c9e4;
    --photo-pink: #f1c7d3;
  }
  * { margin: 0; padding: 0; box-sizing: border-box; }
  html, body {
    width: 1200px; height: 1200px; overflow: hidden;
    background: var(--backdrop);
    font-family: "Montserrat", Arial, sans-serif;
  }
  .flyer {
    position: absolute; left: 200px; top: 34px;
    width: 800px; height: 1132px;
    background: var(--paper);
    overflow: hidden;
  }
  .flyer-art { position: absolute; inset: 0; width: 800px; height: 1132px; }
  .brand-name {
    position: absolute; right: 36px; top: 36px;
    font-weight: 800; font-size: 40px; letter-spacing: 1px;
    color: var(--brand-blue);
  }
  .about { position: absolute; left: 380px; top: 425px; width: 356px; }
  .about-title {
    font-weight: 700; font-size: 28px; color: var(--brand-blue);
    margin-bottom: 10px;
  }
  .about-text {
    font-weight: 300; font-size: 14px; line-height: 20.8px;
    color: var(--ink-soft); text-align: justify;
  }
  .specialties-title {
    margin-top: 20px;
    font-weight: 800; font-style: italic; font-size: 15.5px; line-height: 21px;
    color: var(--brand-blue); text-transform: uppercase;
  }
  .specialties { list-style: none; margin-top: 8px; }
  .specialties li {
    display: flex; align-items: center; gap: 9px;
    font-size: 16.5px; font-weight: 400; color: var(--ink);
    height: 22.8px;
  }
  .tick { width: 15px; height: 15px; flex: none; }
  .features { position: absolute; left: 68px; top: 802px; width: 460px; }
  .features-title {
    font-weight: 700; font-size: 21px; color: var(--brand-blue);
    margin-bottom: 3px;
  }
  .features-list { list-style: none; }
  .features-list li {
    font-size: 14.6px; font-weight: 500; color: var(--ink);
    line-height: 21px; white-space: nowrap;
  }
  .contact {
    position: absolute; top: 1028px;
    display: flex; align-items: center; gap: 14px;
  }
  .contact-call { left: 48px; }
  .contact-web { left: 422px; }
  .contact-icon { width: 46px; height: 46px; flex: none; }
  .contact-label {
    font-size: 21px; font-weight: 500; color: var(--brand-yellow);
    line-height: 22px;
  }
  .contact-value {
    font-size: 36px; font-weight: 500; color: var(--paper);
    line-height: 38px;
  }
</style>
</head>
<body>
<main class="flyer">
  <svg class="flyer-art" viewBox="0 0 800 1132" aria-hidden="false">
    <defs>
      <linearGradient id="heroTone" x1="0" y1="0" x2="1" y2="0.4">
        <stop offset="0" stop-color="#eef0f3"/>
        <stop offset="0.4" stop-color="#c7d4ee"/>
        <stop offset="0.7" stop-color="#e3e7ee"/>
        <stop offset="1" stop-color="var(--photo-pink)"/>
      </linearGradient>
      <linearGradient id="scanTone" x1="0" y1="0" x2="1" y2="1">
        <stop offset="0" stop-color="#c9d6e6"/>
        <stop offset="0.6" stop-color="#eef2f7"/>
        <stop offset="1" stop-color="#b8c3d2"/>
      </linearGradient>
      <linearGradient id="momTone" x1="0" y1="0" x2="1" y2="0">
        <stop offset="0" stop-color="var(--brand-yellow)"/>
        <stop offset="1" stop-color="#c9962a"/>
      </linearGradient>
    </defs>

    <!-- hero photo area -->
    <path role="img" aria-label="Photo: sonographer showing an ultrasound scan on a monitor to a pregnant patient"
          d="M0 0 H800 V438 Q400 294 0 438 Z" fill="url(#heroTone)"/>
    <!-- header swoosh with brand -->
    <path d="M320 0 Q470 150 800 110 V0 Z" fill="var(--paper)"/>
    <path d="M320 0 Q470 150 800 110" fill="none" stroke="var(--brand-yellow)" stroke-width="7"/>
    <path d="M0 438 Q400 294 800 438" fill="none" stroke="var(--brand-yellow)" stroke-width="9"/>

    <!-- circular scan photo -->
    <circle role="img" aria-label="Photo: ultrasound probe scanning a patient's neck"
            cx="197" cy="594" r="158" fill="url(#scanTone)"/>
    <circle cx="197" cy="594" r="158" fill="none" stroke="var(--brand-blue)" stroke-width="5"/>

    <!-- bottom band -->
    <path d="M0 925 Q400 862 800 925 V1132 H0 Z" fill="var(--brand-blue)"/>
    <path d="M0 925 Q400 862 800 925" fill="none" stroke="var(--brand-yellow)" stroke-width="7"/>

    <!-- features panel -->
    <rect x="46" y="795" width="704" height="180" rx="8" fill="var(--brand-yellow)"/>
    <path role="img" aria-label="Photo: expectant mother holding a strip of ultrasound prints"
          d="M491 795 H742 A8 8 0 0 1 750 803 V967 A8 8 0 0 1 742 975 H491 Z" fill="url(#momTone)"/>
  </svg>

  <div class="brand-name">Vero M.Q.</div>

  <section class="about">
    <h2 class="about-title">ABOUT US</h2>
    <p class="about-text">Vero M.Q. is a concierge ultrasound company that provides onsite or offsite diagnostic ultrasounds. We have over 14 years experience in sonography, business management, and customer service. We offer both the physician and patient flexibility, convenience, and access to timely services.</p>
    <h3 class="specialties-title">We provide ultrasounds<br>for the following specialties:</h3>
    <ul class="specialties">
      <li><svg class="tick" viewBox="0 0 16 16"><circle cx="8" cy="8" r="8" fill="var(--brand-yellow)"/><path d="M4.5 8.2 7 10.6 11.6 5.6" fill="none" stroke="#fff" stroke-width="2" stroke-linecap="round" stroke-linejoin="round"/></svg>Obstetrics/ Gynecology</li>
      <li><svg class="tick" viewBox="0 0 16 16"><circle cx="8" cy="8" r="8" fill="var(--brand-yellow)"/><path d="M4.5 8.2 7 10.6 11.6 5.6" fill="none" stroke="#fff" stroke-width="2" stroke-linecap="round" stroke-linejoin="round"/></svg>Abdominal</li>
      <li><svg class="tick" viewBox="0 0 16 16"><circle cx="8" cy="8" r="8" fill="var(--brand-yellow)"/><path d="M4.5 8.2 7 10.6 11.6 5.6" fill="none" stroke="#fff" stroke-width="2" stroke-linecap="round" stroke-linejoin="round"/></svg>Small Parts</li>
      <li><svg class="tick" viewBox="0 0 16 16"><circle cx="8" cy="8" r="8" fill="var(--brand-yellow)"/><path d="M4.5 8.2 7 10.6 11.6 5.6" fill="none" stroke="#fff" stroke-width="2" stroke-linecap="round" stroke-linejoin="round"/></svg>Vascular</li>
    </ul>
  </section>

  <section class="features">
    <h2 class="features-title">FEATURES:</h2>
    <ol class="features-list">
      <li>1. Onsite or Offsite Scans</li>
      <li>2. Images Available Immediately for Referring Physician &amp; Patient</li>
      <li>3. Flexible Options for Ultrasound Interpretation/Billing</li>
      <li>4. Access to Interpreting Radiologist</li>
      <li>5. Final Report Process - 1-2 Business Days/ 1 hour for STAT.</li>
      <li>6. PACS Storage with Secure Access.</li>
    </ol>
  </section>

  <div class="contact contact-call">
    <svg class="contact-icon" viewBox="0 0 48 48" fill="none" stroke="var(--brand-yellow)" stroke-width="2.6" stroke-linecap="round" stroke-linejoin="round">
      <path d="M10 8 L17 8 L20 17 L15.5 20 C18 26 22 30 28 32.5 L31 28 L40 31 L40 38 C40 40 38 42 36 42 C20 41 7 28 6 12 C6 10 8 8 10 8 Z"/>
      <path d="M28 6 A14 14 0 0 1 42 20"/>
      <path d="M27 12 A8 8 0 0 1 36 21"/>
    </svg>
    <div>
      <div class="contact-label">CALL US</div>
      <div class="contact-value">123-456-7890</div>
    </div>
  </div>

  <div class="contact contact-web">
    <svg class="contact-icon" viewBox="0 0 48 48">
      <circle cx="24" cy="24" r="22" fill="var(--brand-yellow)"/>
      <path d="M12 14 C16 12 20 14 19 18 C18 22 14 20 13 25 C12 29 16 31 15 36 C10 32 8 22 12 14 Z" fill="var(--brand-blue)"/>
      <path d="M27 9 C32 10 35 14 33 17 C31 19 27 17 26 21 C25 25 31 25 33 29 C35 33 31 38 28 40 C30 34 26 31 24 28 C21 24 24 20 22 16 C21 13 24 10 27 9 Z" fill="var(--brand-blue)"/>
      <path d="M37 22 C40 24 41 28 39 32 C37 30 36 26 37 22 Z" fill="var(--brand-blue)"/>
    </svg>
    <div>
      <div class="contact-label">VISIT US</div>
      <div class="contact-value">vero-mq.com</div>
    </div>
  </div>
</main>
</body>
</html>
```